Silver Brook Decorators Banner

Create a banner that displays and reinforces Silver Brook Decorators’ brand identity while promoting our interior painting services. The banner will be displayed at indoor venues through the winter. The design should be clean, professional, and visually recognizable to both new and returning customers. See attached design brief & logo source files.

```html
<!DOCTYPE html>
<html lang="en">
<head>
<meta charset="utf-8">
<title>Silver Brook Decorators Banner</title>
<link rel="stylesheet" href="https://fonts.googleapis.com/css2?family=Archivo:wdth,wght@62..125,400..900&display=swap">
<style>
  :root {
    --charcoal: #4a4a48;
    --leaf: #6b9a58;
    --paper: #ffffff;
    --backdrop: #e9ebe8;
    --ink: #474745;
  }
  * { box-sizing: border-box; margin: 0; padding: 0; }
  html, body {
    width: 1200px; height: 879px; overflow: hidden;
    background: var(--backdrop);
    font-family: "Archivo", Arial, sans-serif;
  }
  .banner {
    position: absolute; left: 0; top: 258px;
    width: 1200px; height: 362px;
    background: var(--paper);
    overflow: hidden;
  }
  .brand {
    position: absolute; left: 50px; top: 28px;
    display: flex; align-items: center; gap: 16px;
  }
  .brand-mark {
    width: 26px; height: 26px; background: var(--leaf);
  }
  .brand-name {
    font-weight: 800; font-stretch: 112%;
    font-size: 44px; line-height: 1.05;
    color: var(--leaf);
    letter-spacing: 0.5px;
  }
  .tagline {
    position: absolute; left: 0; width: 630px; top: 150px;
    text-align: center;
    font-weight: 700; font-size: 35px; line-height: 49px;
    color: var(--ink);
    letter-spacing: 0.6px;
  }
  .service-title {
    position: absolute; left: 672px; top: 0;
    width: 498px; height: 152px;
    background: var(--charcoal);
    border-radius: 0 0 30px 30px;
    box-shadow: 0 6px 0 var(--leaf);
    display: flex; flex-direction: column; justify-content: center; align-items: center;
    color: var(--paper);
    font-weight: 800; font-stretch: 125%;
    font-size: 43px; line-height: 46px; letter-spacing: 4px;
    text-align: center;
  }
  .service-list {
    position: absolute; right: 30px; top: 172px;
    list-style: none; text-align: right;
    color: var(--leaf);
    font-weight: 800; font-stretch: 125%;
    font-size: 37px; line-height: 45px; letter-spacing: 2px;
  }
  .cta-band {
    position: absolute; left: 0; top: 306px;
    width: 740px; height: 56px;
    background: var(--charcoal);
    clip-path: polygon(0 0, 700px 0, 740px 100%, 0 100%);
    color: var(--paper);
    font-weight: 700; font-stretch: 75%;
    font-size: 33px; line-height: 56px;
    padding-left: 20px;
  }
  .web-band {
    position: absolute; left: 718px; top: 322px;
    width: 482px; height: 40px;
    background: var(--leaf);
    clip-path: polygon(0 0, 100% 0, 100% 100%, 40px 100%);
    color: var(--paper);
    font-weight: 800; font-size: 28px; line-height: 40px;
    text-align: center; padding-left: 30px;
  }
</style>
</head>
<body>
  <main class="banner">
    <div class="brand">
      <span class="brand-mark"></span>
      <span class="brand-name">Silver Brook<br>Decorators</span>
    </div>
    <p class="tagline">"Paint Smarter" Trusted<br>local professionals,<br>since 2005</p>

    <h1 class="service-title">INTERIOR<br>PAINTING<br>SERVICES</h1>
    <ul class="service-list">
      <li>Walls · Ceilings</li>
      <li>· Trim · Cabinets</li>
      <li>· Drywall Repair</li>
    </ul>

    <div class="cta-band">Call to action: Book a Free Estimate at</div>
    <div class="web-band">www.silverbrookdeco.com</div>
  </main>
</body>
</html>
```